Trance Guide Coaching Marketing Materials
Brochure, Postcard, Business Card, Letterhead, Envelope
I've been in non-stop meetings all week, and I apologize for not being quicker with feedback. I'll comment again this evening. Thank you.
I find myself tied up today on other business. I extended the project a couple of days. This will be the only extension. I will choose a winner promptly when the contest closes, as I did with my previous projects. There may be some final tweaking but everything will be completed within a week of closing, no longer than that. I appreciate all your wonderful creative efforts. Thank you, and may you prosper and thrive happily. Kindest regards.
#22 and #8 good but the people shown have no context. The people depicted should be going about their positive activity or business and not necessarily looking directly into the camera.
#23 interesting design but the people are too frenetic, too much energy. Thank you.
Lots of quality work here, everyone. Thank you. Keep on keepin' on. I will review more this evening (EST) and will extend the contest a day or two at least. The entries are very good. I have to be away from my desk the rest of the day, but I will return here later.
#19 try replacing the guy with outstretched arms. He's cool but we should see more ideas in that spot. Play with it.
I'll talk about other designs later today, as indicated in my earlier note. thanks again.
I have a lot to review today. Thank you for your excellent efforts. I may not comment further until this evening, but please keep on keepin' on.
I am considering extending the contest a few days to give everyone time to react to the comments I make later.
Good work, everyone. Thank you.
I meant #6 quite excellent in below comment today (not #4, which was discussed earlier). Sorry for any confusion. Thank you for the effort.
I may have to extend this contest.
#7 I like this, too. Very good, but needs more variety of people. Tricky but that's why you're the designer! Thank you for the effort.
#4 quite excellent. I'm liking it, but it needs something, not sure what. I see 3 out 5 people white, including both women white. Try mixing it up if you can, although I see from a design point of view the poses and angles work. It could be close.
#3 I gave it 3 stars because the designs are good except for the groups of people, which I already talked about. I want to encourage you, though.
Draft #4, the picture of the guy is interesting. I have to sleep on that one.
Draft #3 and #4: About pictures: I'm not looking for groups of people, and I'm not looking for abstract settings. Pictures should feature individuals in typical settings. Examples: business man, business woman, musician, athlete, teacher, sales person. No couples, no groups. Individuals with whom people reading the brochure can identify.
Thank you.
Thank you for your entries. I'll be reviewing entries tomorrow and offering suggestions.
Designers: Logo AI has been uploaded. Please refer to the Creative Brief and proceed. - Dave
Trance Guide Coaching Contact Info
Gordon P Whitfield CLC CCH
4629 Larkmoor Rd Ste 310
Albany NY 12203
phone 518-926-3081
fax 888-547-2263
web http://TranceGuideNow.example

```html
<!DOCTYPE html>
<html lang="en">
<head>
<meta charset="utf-8">
<title>Trance Guide Coaching – Stationery Set</title>
<link href="https://fonts.googleapis.com/css2?family=Open+Sans:wght@400;600;700&display=swap" rel="stylesheet">
<style>
  :root{
    --navy:#1d3f8a;
    --green:#5a9a2a;
    --green-light:#8cc63f;
    --paper:#ffffff;
    --ink:#3a3a3a;
    --muted:#8a8f99;
    --stage:#e9e6e1;
    --photo-a:#b9a38f;
    --photo-b:#7f8fa6;
    --photo-c:#c9b8a3;
    --photo-d:#8ea0b5;
    --sky:#9cc3e6;
  }
  *{box-sizing:border-box;margin:0;padding:0}
  html,body{width:1200px;height:787px;overflow:hidden}
  body{background:var(--stage);font-family:"Open Sans",Arial,sans-serif;color:var(--ink);position:relative}
  .piece{position:absolute;background:var(--paper);box-shadow:0 2px 6px rgba(0,0,0,.25);overflow:hidden}
  .piece svg.bg{position:absolute;inset:0;width:100%;height:100%}
  .layer{position:absolute}
  .brand{display:flex;align-items:center;gap:4px;font-weight:700;color:var(--navy);white-space:nowrap;line-height:1}
  .brand .dot{border-radius:50%;background:var(--green);flex:none}
  .tiny{font-size:5px;line-height:1.4}
  .tiny + .tiny{margin-top:4px}
  .column-text{position:absolute;width:122px}
  .column-text p{font-size:5px;line-height:1.45;margin-bottom:5px}
  .heading-tag{background:var(--green);color:#fff;font-weight:700;font-size:6px;letter-spacing:.5px;padding:2px 6px;text-align:center}
  .bullets{list-style:none}
  .bullets li{font-size:5px;line-height:1;margin-bottom:5px;display:flex;align-items:center;gap:4px;white-space:nowrap}
  .bullets li::before{content:"";width:5px;height:5px;border-radius:50%;background:var(--green-light);flex:none}
  .contact{font-size:5px;line-height:1.45;color:var(--ink)}
  .contact strong{color:var(--navy);font-size:6px}
  .url{font-size:5px;color:#fff}
  .photo{position:absolute}

  .brochure-outside{left:24px;top:19px;width:312px;height:209px}
  .brochure-inside{left:24px;top:389px;width:427px;height:367px}
  .postcard-front{left:475px;top:60px;width:269px;height:163px}
  .postcard-back{left:475px;top:245px;width:269px;height:163px}
  .business-card{left:566px;top:439px;width:87px;height:55px}
  .letterhead{left:835px;top:48px;width:305px;height:432px}
  .envelope-front{left:475px;top:540px;width:336px;height:156px}
  .envelope-back{left:835px;top:540px;width:322px;height:156px}
</style>
</head>
<body>

<!-- Brochure outside -->
<section class="piece brochure-outside">
  <svg class="bg" viewBox="0 0 312 209" preserveAspectRatio="none">
    <rect x="0" y="0" width="312" height="90" fill="var(--navy)"/>
    <path d="M0 90 Q120 60 190 110 Q250 150 312 95 L312 209 L0 209Z" fill="var(--paper)"/>
    <path d="M0 88 Q120 58 190 108 Q250 148 312 93" fill="none" stroke="var(--green)" stroke-width="6"/>
    <circle cx="160" cy="62" r="58" fill="var(--green)"/>
  </svg>
  <div class="photo" role="img" aria-label="Portrait of a business woman at work" style="left:110px;top:12px;width:48px;height:48px;background:var(--photo-a);border-radius:48px 0 0 0"></div>
  <div class="photo" role="img" aria-label="Portrait of a business man in an office" style="left:162px;top:12px;width:48px;height:48px;background:var(--photo-b);border-radius:0 48px 0 0"></div>
  <div class="photo" role="img" aria-label="Athlete celebrating outdoors" style="left:110px;top:64px;width:48px;height:48px;background:var(--photo-d);border-radius:0 0 0 48px"></div>
  <div class="photo" role="img" aria-label="Salesperson speaking with a client" style="left:162px;top:64px;width:48px;height:48px;background:var(--photo-c);border-radius:0 0 48px 0"></div>

  <div class="layer heading-tag" style="left:8px;top:6px;width:88px">HEADING GOES HERE</div>
  <p class="layer tiny" style="left:8px;top:20px;width:92px;color:#fff">Guided sessions help you build calm focus, steady habits and lasting confidence for daily life.</p>
  <span class="layer url" style="left:226px;top:5px">http://TranceGuideNow.example</span>

  <ul class="layer bullets" style="left:8px;top:104px">
    <li>Bullet item goes here</li><li>Bullet item goes here</li><li>Bullet item goes here</li><li>Bullet item goes here</li>
    <li>Bullet item goes here</li><li>Bullet item goes here</li><li>Bullet item goes here</li><li>Bullet item goes here</li>
  </ul>

  <div class="layer brand" style="left:112px;top:130px;font-size:10px"><span class="dot" style="width:8px;height:8px"></span>Trance Guide Coaching</div>
  <div class="layer contact" style="left:128px;top:148px">
    <strong>Gordon P Whitfield CLC CCH</strong><br>
    4629 Larkmoor Rd Ste 310<br>Albany NY 12203<br>
    P 518-926-3081<br>F 888-547-2263
  </div>
</section>

<!-- Brochure inside -->
<section class="piece brochure-inside">
  <svg class="bg" viewBox="0 0 427 367" preserveAspectRatio="none">
    <path d="M0 275 Q120 240 220 290 Q330 340 427 255 L427 367 L0 367Z" fill="var(--navy)"/>
    <path d="M0 273 Q120 238 220 288 Q330 338 427 253" fill="none" stroke="var(--green)" stroke-width="6"/>
    <circle cx="232" cy="238" r="64" fill="var(--green)"/>
  </svg>
  <div class="photo" role="img" aria-label="Woman with arms outstretched under an open sky" style="left:0;top:262px;width:172px;height:105px;background:linear-gradient(var(--sky),#d9ecf8 70%,#9fc36a)"></div>
  <div class="photo" role="img" aria-label="Teacher in a classroom" style="left:176px;top:182px;width:54px;height:54px;background:var(--photo-a);border-radius:54px 0 0 0"></div>
  <div class="photo" role="img" aria-label="Musician playing an instrument" style="left:234px;top:182px;width:54px;height:54px;background:var(--photo-b);border-radius:0 54px 0 0"></div>
  <div class="photo" role="img" aria-label="Business woman on a phone call" style="left:176px;top:240px;width:54px;height:54px;background:var(--photo-d);border-radius:0 0 0 54px"></div>
  <div class="photo" role="img" aria-label="Business man reviewing notes" style="left:234px;top:240px;width:54px;height:54px;background:var(--photo-c);border-radius:0 0 54px 0"></div>

  <div class="layer heading-tag" style="left:10px;top:10px;width:122px">HEADING GOES HERE</div>
  <div class="layer heading-tag" style="left:153px;top:10px;width:122px">HEADING GOES HERE</div>
  <div class="layer heading-tag" style="left:296px;top:10px;width:122px">HEADING GOES HERE</div>

  <div class="column-text" style="left:10px;top:28px">
    <p>Sessions are tailored to your goals and move at a pace that feels right for you, building calm focus and steady confidence.</p>
    <p>Each meeting blends simple breathing, guided imagery and clear steps you can practise at home between visits.</p>
    <p>Clients leave with practical tools for stress, sleep, habits and performance at work, on stage or in sport.</p>
  </div>
  <ul class="layer bullets" style="left:10px;top:150px">
    <li>Bullet item goes here</li><li>Bullet item goes here</li><li>Bullet item goes here</li><li>Bullet item goes here</li><li>Bullet item goes here</li><li>Bullet item goes here</li>
  </ul>

  <div class="column-text" style="left:153px;top:28px">
    <p>Change begins with a quiet mind. Our coaching helps you notice old patterns and replace them with new choices.</p>
    <p>Whether you lead a team, teach a class or play music, focused practice brings lasting results.</p>
    <p>Sessions are offered in person or online, with flexible times to suit busy weekly schedules.</p>
  </div>

  <div class="column-text" style="left:296px;top:28px">
    <p>Set clear goals, track your progress and celebrate each step forward with support from a trained coach.</p>
    <p>Call today to book a first session and learn how guided focus can help you reach your next milestone.</p>
  </div>
  <ul class="layer bullets" style="left:296px;top:118px">
    <li>Bullet item goes here</li><li>Bullet item goes here</li><li>Bullet item goes here</li><li>Bullet item goes here</li><li>Bullet item goes here</li><li>Bullet item goes here</li>
  </ul>
  <ul class="layer bullets" style="left:362px;top:118px">
    <li>Bullet item here</li><li>Bullet item here</li><li>Bullet item here</li><li>Bullet item here</li><li>Bullet item here</li><li>Bullet item here</li>
  </ul>

  <div class="layer brand" style="left:300px;top:318px;font-size:10px;color:#fff"><span class="dot" style="width:8px;height:8px"></span>Trance Guide Coaching</div>
  <span class="layer url" style="left:312px;top:350px">http://TranceGuideNow.example</span>
</section>

<!-- Postcard front -->
<section class="piece postcard-front">
  <svg class="bg" viewBox="0 0 269 163" preserveAspectRatio="none">
    <rect width="269" height="163" fill="var(--navy)"/>
    <path d="M0 120 Q120 95 269 140 L269 163 L0 163Z" fill="var(--green)"/>
  </svg>
  <div class="photo" role="img" aria-label="Business woman smiling" style="left:82px;top:8px;width:45px;height:45px;background:var(--photo-a)"></div>
  <div class="photo" role="img" aria-label="Business man at a desk" style="left:130px;top:8px;width:45px;height:45px;background:var(--photo-b)"></div>
  <div class="photo" role="img" aria-label="Athlete training" style="left:82px;top:56px;width:45px;height:45px;background:var(--photo-d)"></div>
  <div class="photo" role="img" aria-label="Musician performing" style="left:130px;top:56px;width:45px;height:45px;background:var(--photo-c)"></div>
  <div class="layer brand" style="left:12px;top:100px;font-size:11px;color:#fff"><span class="dot" style="width:8px;height:8px"></span>Trance Guide Coaching</div>
</section>

<!-- Postcard back -->
<section class="piece postcard-back">
  <div class="layer brand" style="left:10px;top:12px;font-size:8px"><span class="dot" style="width:6px;height:6px"></span>Trance Guide Coaching</div>
  <div class="layer contact" style="left:10px;top:26px">4629 Larkmoor Rd Ste 310<br>Albany NY 12203</div>
  <svg class="layer" style="left:131px;top:20px" width="10" height="130" viewBox="0 0 10 130">
    <line x1="5" y1="0" x2="5" y2="130" stroke="var(--green)" stroke-width="1.5"/>
    <circle cx="5" cy="5" r="3" fill="var(--green)"/>
  </svg>
</section>

<!-- Business card -->
<section class="piece business-card">
  <svg class="bg" viewBox="0 0 87 55" preserveAspectRatio="none">
    <path d="M0 38 Q40 28 87 40 L87 55 L0 55Z" fill="var(--navy)"/>
    <path d="M0 37 Q40 27 87 39" fill="none" stroke="var(--green)" stroke-width="2"/>
  </svg>
  <div class="layer brand" style="left:5px;top:7px;font-size:5px"><span class="dot" style="width:4px;height:4px"></span>Trance Guide Coaching</div>
  <div class="layer contact" style="left:5px;top:42px;font-size:3.5px;color:#fff">Gordon P Whitfield CLC CCH<br>518-926-3081</div>
</section>

<!-- Letterhead -->
<section class="piece letterhead">
  <svg class="bg" viewBox="0 0 305 432" preserveAspectRatio="none">
    <path d="M0 0 L40 0 Q10 20 0 60Z" fill="var(--green)"/>
  </svg>
  <div class="layer brand" style="left:168px;top:24px;font-size:9px"><span class="dot" style="width:7px;height:7px"></span>Trance Guide Coaching</div>
  <div class="layer contact" style="left:180px;top:38px">4629 Larkmoor Rd Ste 310<br>Albany NY 12203</div>
  <div class="layer contact" style="left:60px;top:410px;color:var(--muted)">518-926-3081 · 888-547-2263 · http://TranceGuideNow.example</div>
</section>

<!-- Envelope front -->
<section class="piece envelope-front">
  <svg class="bg" viewBox="0 0 336 156" preserveAspectRatio="none">
    <path d="M0 0 L50 0 Q14 14 0 50Z" fill="var(--green)"/>
  </svg>
  <div class="layer brand" style="left:14px;top:12px;font-size:10px"><span class="dot" style="width:8px;height:8px"></span>Trance Guide Coaching</div>
  <div class="layer contact" style="left:26px;top:28px">4629 Larkmoor Rd Ste 310<br>Albany NY 12203</div>
</section>

<!-- Envelope back -->
<section class="piece envelope-back">
  <svg class="bg" viewBox="0 0 322 156" preserveAspectRatio="none">
    <path d="M0 0 L161 80 L322 0" fill="none" stroke="#d5d5d5" stroke-width="1"/>
    <path d="M0 156 L140 70 M322 156 L182 70" fill="none" stroke="#e2e2e2" stroke-width="1"/>
  </svg>
  <div class="layer brand" style="left:122px;top:12px;font-size:8px"><span class="dot" style="width:6px;height:6px"></span>Trance Guide Coaching</div>
  <div class="layer contact" style="left:134px;top:24px;font-size:4px">4629 Larkmoor Rd Ste 310<br>Albany NY 12203</div>
</section>

</body>
</html>
```